Bref créative
Ostravelde German Shepherds
West Bloodline German Shepherds
Bright & Fun-filled
Torsten Ebbelmann
287 Murow Rd
Suite F.
Wendholt, Ks 79152
torsten@ostravelde-kennel.example
www.ostravelde-kennel.example
Logo blown up, and some creativity.
Heres the logo. If you could make the German Shepherd text black that would be awesome. Currently with it being yellow it doesnt stick out enough. See what you can do. Thanks!
Not sure if zip file works? So just going to do this....

```html
<!DOCTYPE html>
<html lang="en">
<head>
<meta charset="utf-8">
<title>Ostravelde German Shepherds – Business Card</title>
<link rel="stylesheet" href="https://fonts.googleapis.com/css2?family=Arimo:wght@400;700&display=swap">
<style>
  :root {
    --backdrop: #e6e3de;
    --card-black: #0b0b0b;
    --gold-light: #f6c83a;
    --gold-mid: #e8a90f;
    --gold-deep: #c98a05;
    --silver: #9a9a9a;
    --white: #ffffff;
    --muted: #d4d4d4;
  }
  * { box-sizing: border-box; margin: 0; padding: 0; }
  html, body { width: 1200px; height: 821px; overflow: hidden; }
  body {
    background: var(--backdrop);
    font-family: "Arimo", Arial, sans-serif;
    position: relative;
  }
  .card {
    position: absolute;
    top: 256px;
    width: 540px;
    height: 309px;
    background: var(--card-black);
    overflow: hidden;
    box-shadow: 0 6px 18px rgba(0,0,0,0.25);
  }
  .card--front { left: 40px; }
  .card--back { left: 620px; }

  /* Front side */
  .gold-panel {
    position: absolute;
    left: 200px; top: 0;
    width: 340px; height: 268px;
    background: linear-gradient(135deg, var(--gold-light) 0%, var(--gold-mid) 55%, var(--gold-deep) 100%);
    clip-path: polygon(12% 0, 100% 0, 100% 100%, 0 100%, 0 12%);
  }
  .silhouette-area {
    position: absolute;
    left: 150px; top: 18px;
    width: 120px; height: 250px;
    background: linear-gradient(180deg, #1a1a1a 0%, #050505 100%);
    border-right: 3px solid var(--silver);
    border-radius: 0 60px 30px 0;
  }
  .contact {
    position: absolute;
    left: 24px; top: 70px;
    color: var(--white);
  }
  .contact__name {
    font-size: 22px;
    font-weight: 700;
    margin-bottom: 24px;
  }
  .contact__address {
    font-size: 10px;
    line-height: 15px;
    color: var(--muted);
    margin-bottom: 18px;
  }
  .contact__list { list-style: none; font-size: 10px; color: var(--muted); }
  .contact__list li {
    display: flex; align-items: center; gap: 8px;
    height: 17px;
  }
  .contact__list svg { width: 11px; height: 11px; fill: var(--white); flex: none; }
  .website {
    position: absolute;
    left: 205px; bottom: 14px;
    font-size: 9px;
    letter-spacing: 2px;
    color: var(--white);
  }

  /* Brand lockup */
  .brand {
    position: absolute;
    display: flex; flex-direction: column; align-items: center;
    font-weight: 700;
    text-align: center;
  }
  .brand__square {
    width: 56px; height: 56px;
    border-radius: 6px;
    margin-bottom: 10px;
  }
  .brand__name { font-size: 22px; letter-spacing: 1px; line-height: 1.1; }
  .brand__tag { font-size: 10px; letter-spacing: 3px; margin-top: 3px; }

  .brand--front { left: 280px; top: 70px; width: 220px; color: var(--card-black); }
  .brand--front .brand__square { background: var(--card-black); }

  .brand--back { left: 160px; top: 88px; width: 220px; color: var(--white); }
  .brand--back .brand__square { background: var(--gold-mid); }
</style>
</head>
<body>
  <section class="card card--front" aria-label="Business card front">
    <div class="gold-panel"></div>
    <div class="silhouette-area" role="img" aria-label="Black German Shepherd head silhouette in profile with silver outline"></div>

    <div class="contact">
      <p class="contact__name">Torsten Ebbelmann</p>
      <p class="contact__address">287 Murow Rd Suite F.<br>Wendholt, Ks 79152</p>
      <ul class="contact__list">
        <li><svg viewBox="0 0 24 24"><path d="M6.6 10.8a15 15 0 0 0 6.6 6.6l2.2-2.2a1 1 0 0 1 1-.25 11.4 11.4 0 0 0 3.6.57 1 1 0 0 1 1 1V20a1 1 0 0 1-1 1A17 17 0 0 1 3 4a1 1 0 0 1 1-1h3.5a1 1 0 0 1 1 1c0 1.25.2 2.45.57 3.57a1 1 0 0 1-.25 1z"/></svg>(555) 014-2268</li>
        <li><svg viewBox="0 0 24 24"><path d="M7 2h10a1 1 0 0 1 1 1v18a1 1 0 0 1-1 1H7a1 1 0 0 1-1-1V3a1 1 0 0 1 1-1zm1 3v12h8V5z"/></svg>(555) 018-7730</li>
        <li><svg viewBox="0 0 24 24"><path d="M2 5h20v14H2zm2 2v.5l8 5 8-5V7zm0 3v7h16v-7l-8 5z"/></svg>torsten@ostravelde-kennel.example</li>
      </ul>
    </div>

    <div class="brand brand--front">
      <div class="brand__square"></div>
      <p class="brand__name">OSTRAVELDE</p>
      <p class="brand__tag">GERMAN SHEPHERDS</p>
    </div>

    <p class="website">www.ostravelde-kennel.example</p>
  </section>

  <section class="card card--back" aria-label="Business card back">
    <div class="brand brand--back">
      <div class="brand__square"></div>
      <p class="brand__name">OSTRAVELDE</p>
      <p class="brand__tag">GERMAN SHEPHERDS</p>
    </div>
  </section>
</body>
</html>
```